Design gusset bag packaging for a high protein cake mix

We need packaging designed for a 4x6x2 3/8 silver metallic bag. It will hold high protein cake mix. I will attach current label designs that we have on the back. I want it to be catchy-- template will be posted as well. Please stick to 6 printing colors or less.

Target Market(s)

Fitness, diet, dessert

Font styles to use
Serif
Decorative
Script

Colors
86cfc6
87d0c7
33b8a4
f0494f
fbf289
f59195
85cae6

Requirements
Must have
• It must include the nutrition label. I will attach our current label. Must have our logo. Please change the title to Wee Fern Bakery Cake Mix (it's in red on the label) and change applesauce serving to 1/2 cup from "1 serving". Please stick to 6 printing colors or less.
Nice to have
• Would love to top flap above the zipper to say Eat Cake, Get Fern! And on the back top flap say "Sprinkles- Enjoy the little things in life" Would love to have some sprinkles scattered around the front of the package..maybe even to look like it's coming out of a sprinkle shaker. Please feel free to use a more modern looking font

```html
<!DOCTYPE html>
<html lang="en">
<head>
<meta charset="utf-8">
<title>Wee Fern Bakery Cake Mix – Pouch</title>
<link href="https://fonts.googleapis.com/css2?family=Luckiest+Guy&family=Oswald:wght@400&family=Open+Sans:wght@400;600;700&family=Arimo:wght@400;700&display=swap" rel="stylesheet">
<style>
:root{
  --bg:#e6e7e9;
  --bag:#ffffff;
  --teal:#86cfc6;
  --teal-light:#aee3de;
  --teal-deep:#33b8a4;
  --red:#f0494f;
  --pink:#f59195;
  --yellow:#fbf289;
  --sky:#85cae6;
  --ink:#222222;
  --zip:#eceef0;
}
*{margin:0;padding:0;box-sizing:border-box}
html,body{width:1200px;height:969px;overflow:hidden;background:var(--bg)}
.canvas{position:relative;width:1200px;height:969px}
.pouch{position:absolute;top:216px;height:532px;background:var(--bag);box-shadow:0 14px 18px -12px rgba(0,0,0,.25);overflow:hidden}
.pouch--front{left:234px;width:352px}
.pouch--back{left:624px;width:340px}
.sprinkle-field{position:absolute;left:0;right:0;top:0;bottom:36px;
  background:
    radial-gradient(circle at 20% 35%,rgba(240,73,79,.16),transparent 35%),
    radial-gradient(circle at 80% 30%,rgba(134,207,198,.28),transparent 35%),
    radial-gradient(circle at 25% 75%,rgba(251,242,137,.35),transparent 35%),
    radial-gradient(circle at 78% 70%,rgba(245,145,149,.22),transparent 35%),
    radial-gradient(circle at 50% 10%,rgba(133,202,230,.2),transparent 35%)}
.zipper{position:absolute;left:0;right:0;top:104px;height:40px;background:repeating-linear-gradient(var(--zip) 0 6px,#f7f8f9 6px 12px)}
.base-band{position:absolute;left:0;right:0;bottom:0;height:36px;background:var(--teal-light)}
.flap-slogan{position:absolute;top:54px;left:0;right:0;text-align:center;font-family:"Luckiest Guy",cursive;font-size:34px;line-height:40px;color:var(--teal-deep);letter-spacing:.5px;white-space:nowrap}
.brand-mark{position:absolute;top:178px;left:50%;width:56px;height:56px;margin-left:-28px;border-radius:50%;background:var(--sky)}
.brand-name{position:absolute;top:248px;left:0;right:0;text-align:center;font-family:"Oswald",sans-serif;font-size:44px;line-height:48px;color:var(--ink)}
.ribbon{position:absolute;top:398px;left:58px;width:270px;height:62px;background:var(--teal-light);transform:rotate(-8deg);display:flex;align-items:center;justify-content:center}
.ribbon-text{font-family:"Luckiest Guy",cursive;font-size:36px;line-height:40px;color:var(--pink);white-space:nowrap}
.web{position:absolute;bottom:8px;left:0;right:0;text-align:center;font-family:"Open Sans",sans-serif;font-size:15px;font-weight:600;letter-spacing:1px;color:var(--ink)}
.info-col{position:absolute;left:30px;top:156px;width:146px;font-family:"Open Sans",sans-serif;font-size:7.4px;line-height:8.6px;color:var(--ink)}
.product-title{text-align:center;font-size:14px;line-height:17px;color:var(--red);font-weight:400}
.back-mark{width:30px;height:30px;border-radius:50%;background:var(--sky);margin:8px auto 0}
.back-name{text-align:center;font-family:"Oswald",sans-serif;font-size:24px;line-height:26px;margin-top:4px}
.info-col h3{font-size:7.6px;font-weight:700;margin-top:8px}
.info-col p{text-align:justify}
.ingredients{margin-top:8px}
.net-wt{margin-top:8px;font-size:9px;font-weight:600}
.facts{position:absolute;left:184px;top:154px;width:126px;border:1px solid var(--ink);padding:2px 3px;font-family:"Arimo",sans-serif;font-size:5.6px;line-height:7.2px;color:var(--ink);background:#fff}
.facts h2{font-size:14px;line-height:15px;font-weight:700}
.rule-thick{border-top:4px solid var(--ink);margin:2px 0}
.rule-mid{border-top:2px solid var(--ink);margin:1px 0}
.row{display:flex;justify-content:space-between;border-top:.5px solid #999}
.row .v{display:flex;gap:10px}
.row .v span{width:16px;text-align:right}
.b{font-weight:700}
.in{padding-left:6px}
.foot{font-size:4.6px;line-height:5.6px;margin-top:2px}
.address{position:absolute;left:184px;top:452px;width:126px;text-align:center;font-family:"Arimo",sans-serif;font-size:6.2px;line-height:7px;font-weight:700;letter-spacing:.6px;color:var(--ink)}
</style>
</head>
<body>
<div class="canvas">

  <section class="pouch pouch--front">
    <div class="sprinkle-field" role="img" aria-label="Scattered colourful sprinkles"></div>
    <div class="flap-slogan">Eat Cake, Get Fern!</div>
    <div class="zipper"></div>
    <div class="brand-mark"></div>
    <div class="brand-name">Wee Fern<br>Bakery</div>
    <div class="ribbon" role="img" aria-label="Teal ribbon banner"><span class="ribbon-text">CAKE MIX</span></div>
    <div class="base-band"></div>
    <div class="web">www.weefernbakery.com</div>
  </section>

  <section class="pouch pouch--back">
    <div class="sprinkle-field" role="img" aria-label="Scattered colourful sprinkles"></div>
    <div class="zipper"></div>

    <div class="info-col">
      <div class="product-title">Wee Fern Bakery<br>Cake Mix</div>
      <div class="back-mark"></div>
      <div class="back-name">Wee Fern<br>Bakery</div>
      <h3>Baking Instructions:</h3>
      <p>Add 1 egg white (3 Tbsp), 1/2 cup unsweetened applesauce (75g) and 1/8th cup of unsweet cashew milk (30mL/g). Bake in microwave for 2:40</p>
      <p class="ingredients"><b>INGREDIENTS:</b> Whey Protein Blend (Whey Protein Isolate, Whey Protein Concentrate, Whey Protein Hydrosylate), Natural And Artificial Flavors, Salt, Xantham Gum, Sucralose, Essential Fatty Acid Matrix (Medium Chain Triglycerides, Conjugated Linoleic Acid), Digestive Enzyme Complex (Glycoamylase, Amylase, Lipase, Protease, Papain, Hemicellulase, Cellulase, Lactase), Meadow Valley Stevia, Coconut Flour, Organic Golden Flax Seed Meal, Baking Powder (Sodium Acid Pyrophosphate, Sodium Bicarbonate, Cornstarch, Monocalcium Phosphate). Contains Milk</p>
      <div class="net-wt">Net Wt: 2.2 oz (60g)</div>
    </div>

    <div class="facts">
      <h2>Nutrition Facts</h2>
      <div>Serving Size: (60g)<br>Servings Per Container: 1</div>
      <div class="rule-thick"></div>
      <div class="row b"><span>Amount Per Serving</span><span class="v"><span>Mix</span><span>Baked</span></span></div>
      <div class="row b"><span>Calories</span><span class="v"><span>180</span><span>250</span></span></div>
      <div class="row"><span class="in">Calories from Fat</span><span class="v"><span>50</span><span>50</span></span></div>
      <div class="rule-mid"></div>
      <div class="row" style="justify-content:flex-end"><span>% Daily Value**</span></div>
      <div class="row"><span><b>Total Fat</b> 5g*</span><span class="v b"><span>8%</span><span>9%</span></span></div>
      <div class="row"><span class="in">Saturated Fat 2g</span><span class="v b"><span>10%</span><span>10%</span></span></div>
      <div class="row"><span class="in"><i>Trans</i> Fat 0g</span></div>
      <div class="row"><span><b>Cholesterol</b> 55mg</span><span class="v b"><span>18%</span><span>18%</span></span></div>
      <div class="row"><span><b>Sodium</b> 370mg</span><span class="v b"><span>15%</span><span>20%</span></span></div>
      <div class="row"><span><b>Total Carbohydrate</b> 11g</span><span class="v b"><span>4%</span><span>7%</span></span></div>
      <div class="row"><span class="in">Dietary Fiber 7g</span><span class="v b"><span>28%</span><span>32%</span></span></div>
      <div class="row"><span class="in">Sugars 3g</span></div>
      <div class="row b"><span>Protein 26g</span></div>
      <div class="rule-thick"></div>
      <div class="row"><span>Vitamin A</span><span class="v"><span>0%</span><span>2%</span></span></div>
      <div class="row"><span>Vitamin C</span><span class="v"><span>0%</span><span>15%</span></span></div>
      <div class="row"><span>Calcium</span><span class="v"><span>25%</span><span>30%</span></span></div>
      <div class="row"><span>Iron</span><span class="v"><span>6%</span><span>6%</span></span></div>
      <div class="foot">* Amount in Mix<br>**Percent Daily Values are based on a 2,000 calorie diet. Your daily values may be higher or lower depending on your calorie needs.</div>
      <div class="foot">Total Fat less than 65g / 80g · Sat Fat less than 20g / 25g · Cholesterol less than 300mg · Sodium less than 2,400mg · Total Carbohydrate 300g / 375g · Dietary Fiber 25g / 30g</div>
    </div>

    <div class="address">WEE FERN BAKERY<br>PO BOX 52<br>MAPLE RIDGE, OH<br>44990<br>www.weefernbakery.com</div>

    <div class="base-band"></div>
  </section>

</div>
</body>
</html>
```